Slider Map JPG. for website

have a Joomla site that I have built and need a "slider" designed / drawn. I have put something together to give someone an idea of the content I need but obviously I am not skilled at creating a piece that looks good. The final file need to be a 1258 x 400 pixels in a JPG format but I would also like the original format as well in case I need to change later. I have attached 2 files. TVR-Slide.jpg is the slider I want redone and a123 is a screen shot of the website so you can see what is around it. Please feel free to play with size / shape of text and maps and be creative, what I put together was simply the only way I could think to relay what I need. The only part of the map that is relevant to me is the names in yellow with the dark black outlines. The ocean, Canada, and United sates parts do not need to be in the picture if you choose. I would like something that is more modern, crisp and professional looking. Also I am not stuck on the blue color used on the website so if you want me to change that I can. Again be creative but I am looking for a professional look. Thank you

```html
<!DOCTYPE html>
<html lang="en">
<head>
<meta charset="utf-8">
<title>Tri-Valley Reps, Inc.</title>
<link rel="stylesheet" href="https://fonts.googleapis.com/css2?family=Open+Sans:wght@400;600;700&family=Oswald:wght@500;700&family=Archivo+Narrow:wght@400;700&family=Dancing+Script:wght@700&display=swap">
<style>
:root{
  --backdrop:#d9b27c;
  --nav-blue:#2a8ac8;
  --nav-line:#4a9fd4;
  --white:#ffffff;
  --crimson:#c8103e;
  --crimson-light:#e0406a;
  --hero-dark:#2b2b2b;
  --hero-panel:#1f1f1f;
  --bar-black:#121212;
  --content-bg:#f3f3f3;
  --ink:#1d1d1d;
  --muted:#4a4a4a;
  --teal:#3aa89a;
  --search-bg:#efefef;
  --partner-navy:#1c3c7a;
}
*{margin:0;padding:0;box-sizing:border-box}
html,body{width:1200px;height:790px;overflow:hidden}
body{background:var(--backdrop);font-family:"Open Sans",sans-serif;position:relative}
.page{position:absolute;left:50px;top:0;width:1110px;height:790px;background:var(--content-bg);overflow:hidden}
.main-nav{height:52px;background:var(--nav-blue);display:flex}
.main-nav a{flex:1;display:flex;align-items:center;justify-content:center;color:var(--white);text-decoration:none;font-weight:700;font-size:13px;padding-bottom:16px;border-right:1px solid var(--nav-line)}
.main-nav a:last-child{border-right:none}
.main-nav a.current{color:var(--ink)}
.site-header{height:117px;background:var(--white);position:relative}
.brand{position:absolute;left:62px;top:34px;display:flex;align-items:center;gap:10px;color:var(--crimson);font-weight:600;font-size:19px;line-height:1.05}
.brand-dot{width:46px;height:46px;border-radius:50%;background:var(--crimson);flex:none}
.search{position:absolute;right:56px;top:16px;width:188px;height:22px;background:var(--search-bg);border-radius:2px}
.search svg{position:absolute;right:6px;top:5px}
.partner-badge{position:absolute;right:56px;top:54px;width:42px;height:18px;background:var(--partner-navy);border-radius:9px}
.hero{position:relative;height:289px;background:linear-gradient(180deg,#333 0%,var(--hero-dark) 100%)}
.hero-panel{position:absolute;left:670px;top:57px;width:440px;height:179px;background:var(--hero-panel);border-bottom:2px solid var(--crimson)}
.hero-map{position:absolute;left:463px;top:0;width:316px;height:266px;background:linear-gradient(160deg,var(--crimson) 0%,var(--crimson-light) 100%)}
.hero-title{position:absolute;right:710px;top:36px;text-align:right;font-family:"Oswald",sans-serif;font-weight:700;line-height:1;color:var(--white);white-space:nowrap}
.hero-title .l1{font-size:40px}
.hero-title .year{font-size:62px;color:var(--crimson)}
.hero-title .l2{font-size:42px;margin-top:-2px}
.hero-title .red{font-size:33px;color:var(--crimson);margin-top:4px}
.hero-title .region{font-weight:500;font-size:23px;margin-top:10px}
.hero-copy{position:absolute;left:825px;top:68px;color:var(--white);font-family:"Archivo Narrow",sans-serif;font-size:20px;line-height:1.14}
.hero-copy strong{display:block;margin-top:12px;font-weight:700}
.slogan-bar{height:64px;background:var(--bar-black);display:flex;align-items:center;justify-content:space-between;padding:0 86px;color:var(--white);font-weight:700;font-size:18.3px}
.content{display:flex;padding:44px 0 0 56px}
.col{width:339px}
.col h2{font-family:"Dancing Script",cursive;font-size:33px;color:var(--ink);font-weight:700;margin-bottom:10px;line-height:1}
.news-item{display:flex;gap:18px;margin-top:6px;margin-bottom:30px}
.news-thumb{width:89px;height:88px;flex:none;background:linear-gradient(135deg,#8fc6e2,#3b6f8e)}
.news-thumb.battery{background:linear-gradient(135deg,#f2f2f2,#222)}
.news-item a{color:var(--crimson);font-size:13px;line-height:1.25;text-decoration:none;width:200px}
.news-item a.narrow{width:165px}
.company .est{font-size:9px;font-weight:700;color:var(--ink);margin:14px 0 20px}
.company p{font-family:Arial,sans-serif;font-size:11.5px;line-height:1.2;text-align:justify;color:var(--ink);width:321px}
.more-btn{display:inline-block;margin-top:16px;background:var(--crimson);color:var(--white);font-size:9px;font-weight:700;padding:6px 13px;text-decoration:none}
.request dl{margin-left:18px;margin-top:8px}
.request dt{color:var(--teal);font-size:9.5px;margin-top:18px}
.request dt:first-child{margin-top:0}
.request dd{font-size:9.5px;line-height:1.3;color:var(--muted);width:300px}
</style>
</head>
<body>
<div class="page">
  <nav class="main-nav">
    <a class="current" href="#">MAIN PAGE</a>
    <a href="#">ABOUT US</a>
    <a href="#">DISTRIBUTORS</a>
    <a href="#">LATEST NEWS</a>
    <a href="#">REQUEST</a>
    <a href="#">CONTACT US</a>
  </nav>
  <header class="site-header">
    <div class="brand"><span class="brand-dot"></span><span>Tri-Valley<br>Reps, Inc.</span></div>
    <div class="search"><svg width="10" height="10" viewBox="0 0 10 10"><circle cx="4" cy="4" r="3" fill="none" stroke="#666" stroke-width="1.3"/><line x1="6.2" y1="6.2" x2="9.2" y2="9.2" stroke="#666" stroke-width="1.5"/></svg></div>
    <div class="partner-badge"></div>
  </header>
  <section class="hero">
    <div class="hero-panel"></div>
    <div class="hero-map" role="img" aria-label="Map of the Pacific Northwest states with office locations marked"></div>
    <div class="hero-title">
      <div class="l1">Since <span class="year">1974</span>,</div>
      <div class="l2">TVR has provided a</div>
      <div class="red">trusted and experienced</div>
      <div class="red">high level of service</div>
      <div class="region">IN THE PACIFIC NORTHWEST REGION</div>
    </div>
    <div class="hero-copy">We are conveniently located<br>in Alderport, OR, Cedarfall<br>and Ridgemont, WA.
      <strong>This enables us to bring our<br>principals, distributors and<br>customers outstanding results.</strong>
    </div>
  </section>
  <div class="slogan-bar">
    <svg width="14" height="14" viewBox="0 0 14 14"><path d="M10 1 L4 7 L10 13" fill="none" stroke="#fff" stroke-width="2.4"/></svg>
    <span>ELECTRONIC COMPONENTS MANUFACTURER’S REPRESENTATIVE IN THE PACIFIC NORTHWEST</span>
    <svg width="14" height="14" viewBox="0 0 14 14"><path d="M4 1 L10 7 L4 13" fill="none" stroke="#fff" stroke-width="2.4"/></svg>
  </div>
  <main class="content">
    <section class="col news">
      <h2>Latest News</h2>
      <div class="news-item"><div class="news-thumb" role="img" aria-label="Colored thumbwheel sensor modules"></div><a class="narrow" href="#">COMING SOON!! KX series Proportional Hall effect thumbwheels</a></div>
      <div class="news-item"><div class="news-thumb battery" role="img" aria-label="Lithium polymer battery pack"></div><a href="#">Voltra EasyCell Lithium Polymer Battery Packs Now Stocked and Distributed by Cell Depot</a></div>
    </section>
    <section class="col company">
      <h2>Our Company</h2>
      <div class="est">Established in 1978</div>
      <p>Tri-Valley Reps Inc. (TVR) was founded on the belief that providing our OEM customers, distributors and principals with “above and beyond” service was needed to be a successful manufacturer’s representative. Nearly four decades later, that belief remains unchanged.</p>
      <a class="more-btn" href="#">MORE</a>
    </section>
    <section class="col request">
      <h2>Request</h2>
      <dl>
        <dt>Samples</dt>
        <dd>Samples for your design and testing purposes are available. Most often, at no charge to you.</dd>
        <dt>Quotes</dt>
        <dd>Budgetary or formal quotes are available to assist with your project planning. We can facilitate quotations regardless of the production location.</dd>
        <dt>Engineering Call</dt>
        <dd>Difficult technical questions need answers. We can arrange an engineering meeting with our technical team to help answer these questions.</dd>
      </dl>
    </section>
  </main>
</div>
</body>
</html>
```